Estate Planning Law Firm opening new branch in Florida

I am an experienced estate planning attorney that recently relocated to Florida. Looking for a banner Ad to place on platforms such as YardLoop, Chatterly and Pixmora to create publicity for firm and new leads.

```html
<!DOCTYPE html>
<html lang="en">
<head>
<meta charset="utf-8">
<title>Serenova Law Firm – Estate Planning Banner Set</title>
<link href="https://fonts.googleapis.com/css2?family=Cinzel:wght@400;700&family=Quicksand:wght@500;700&display=swap" rel="stylesheet">
<style>
  :root{
    --ink:#1f2f45;
    --teal:#1e7172;
    --teal-dark:#0f5253;
    --bg-light:#f4f9fa;
    --bg-mint:#e4f0f2;
    --photo-a:#c9d7dc;
    --photo-b:#8d7f82;
    --white:#ffffff;
  }
  *{margin:0;padding:0;box-sizing:border-box}
  html,body{width:1200px;height:981px;overflow:hidden;background:var(--white)}
  body{position:relative;font-family:"Quicksand",sans-serif;color:var(--ink)}

  .banner{position:absolute;overflow:hidden;background:linear-gradient(160deg,var(--bg-light) 0%,var(--bg-mint) 100%)}
  .banner--square{left:160px;top:118px;width:422px;height:422px}
  .banner--wide{left:112px;top:623px;width:470px;height:246px}
  .banner--tall{left:670px;top:118px;width:423px;height:751px}

  .frame{position:absolute;inset:0;width:100%;height:100%}
  .frame path{fill:none;stroke:var(--teal);stroke-width:2}

  .photo{position:absolute}
  .banner--square .photo{left:190px;top:50px;width:232px;height:372px;
    background:linear-gradient(90deg,rgba(201,215,220,0) 0%,var(--photo-a) 30%,var(--photo-b) 100%)}
  .banner--wide .photo{left:230px;top:4px;width:240px;height:242px;
    background:linear-gradient(90deg,rgba(201,215,220,0) 0%,var(--photo-a) 30%,var(--photo-b) 100%)}
  .banner--tall .photo{left:0;top:340px;width:423px;height:411px;
    background:linear-gradient(180deg,rgba(201,215,220,0) 0%,var(--photo-a) 30%,var(--photo-b) 100%)}

  .brand{position:absolute;display:flex;flex-direction:column;align-items:center;font-family:"Cinzel",serif;color:var(--ink)}
  .brand__name{font-weight:700;letter-spacing:.02em;line-height:1}
  .brand__sub{font-family:"Quicksand",sans-serif;font-weight:500;letter-spacing:.02em;margin-top:2px;line-height:1}
  .banner--square .brand{left:48px;top:24px}
  .banner--square .brand__name{font-size:15px}
  .banner--square .brand__sub{font-size:5px}
  .banner--wide .brand{left:46px;top:19px}
  .banner--wide .brand__name{font-size:12px}
  .banner--wide .brand__sub{font-size:4px}
  .banner--tall .brand{left:0;right:0;top:27px}
  .banner--tall .brand__name{font-size:16px}
  .banner--tall .brand__sub{font-size:5.5px}

  .headline{position:absolute;font-family:"Cinzel",serif;font-weight:700;color:var(--ink);white-space:nowrap}
  .headline span{display:block}
  .headline .accent{font-weight:400;color:var(--teal)}
  .banner--square .headline{left:31px;top:76px;font-size:25px;line-height:31px}
  .banner--wide .headline{left:35px;top:51px;font-size:20px;line-height:27px}
  .banner--tall .headline{left:0;right:0;top:77px;text-align:center;font-size:31px;line-height:38.5px}

  .lede{position:absolute;font-weight:500;color:var(--ink)}
  .banner--square .lede{left:31px;top:213px;width:200px;font-size:7.4px;line-height:13px}
  .banner--wide .lede{left:35px;top:166px;width:190px;font-size:6.4px;line-height:10.6px}
  .banner--tall .lede{left:60px;right:60px;top:236px;text-align:center;font-size:8.8px;line-height:14px}

  .cta{position:absolute;display:flex;align-items:center;justify-content:center;border-radius:20px;
    background:linear-gradient(180deg,var(--teal) 0%,var(--teal-dark) 100%);color:var(--white);
    font-weight:700;letter-spacing:.05em;white-space:nowrap}
  .banner--square .cta{left:31px;top:355px;width:160px;height:33px;font-size:7.6px}
  .banner--wide .cta{left:318px;top:200px;width:136px;height:29px;font-size:6.6px}
  .banner--tall .cta{left:132px;top:298px;width:160px;height:32px;font-size:7.6px}
</style>
</head>
<body>

<section class="banner banner--square">
  <svg class="frame" viewBox="0 0 422 422" aria-hidden="true">
    <path d="M40 10H10V412H412V10H140"/>
    <path d="M140 10Q132 10 132 16Q132 21 137 21"/>
  </svg>
  <div class="photo" role="img" aria-label="Smiling attorney in glasses and a checked blazer, arms crossed, with a misty city skyline behind"></div>
  <div class="brand"><span class="brand__name">SERENOVA</span><span class="brand__sub">LAW FIRM, PLLC</span></div>
  <h1 class="headline"><span>Experienced</span><span class="accent">Estate Planning</span><span>Attorney Now</span><span>In Florida</span></h1>
  <p class="lede">Protect your family's future with comprehensive estate planning. Specializing in wills, trusts, and probate services. Schedule your consultation today!</p>
  <a class="cta">BOOK YOUR CONSULTATION</a>
</section>

<section class="banner banner--wide">
  <svg class="frame" viewBox="0 0 470 246" aria-hidden="true">
    <path d="M42 8H8V238H462V8H133"/>
    <path d="M133 8Q126 8 126 13Q126 18 130 18"/>
  </svg>
  <div class="photo" role="img" aria-label="Smiling attorney in glasses and a checked blazer, arms crossed, with a misty city skyline behind"></div>
  <div class="brand"><span class="brand__name">SERENOVA</span><span class="brand__sub">LAW FIRM, PLLC</span></div>
  <h2 class="headline"><span>Experienced</span><span class="accent">Estate Planning</span><span>Attorney Now</span><span>In Florida</span></h2>
  <p class="lede">Protect your family's future with comprehensive estate planning. Specializing in wills, trusts, and probate services. Schedule your consultation today!</p>
  <a class="cta">BOOK YOUR CONSULTATION</a>
</section>

<section class="banner banner--tall">
  <svg class="frame" viewBox="0 0 423 751" aria-hidden="true">
    <path d="M156 10H10V741H413V10H281"/>
    <path d="M281 10Q273 10 273 16Q273 21 278 21"/>
  </svg>
  <div class="photo" role="img" aria-label="Smiling attorney in glasses and a checked blazer, arms crossed, in front of a misty city skyline"></div>
  <div class="brand"><span class="brand__name">SERENOVA</span><span class="brand__sub">LAW FIRM, PLLC</span></div>
  <h2 class="headline"><span>Experienced</span><span class="accent">Estate Planning</span><span>Attorney Now</span><span>In Florida</span></h2>
  <p class="lede">Protect your family's future with comprehensive estate planning. Specializing in wills, trusts, and probate services. Schedule your consultation today!</p>
  <a class="cta">BOOK YOUR CONSULTATION</a>
</section>

</body>
</html>
```